Homes, Invest in Non-performing loans

We need only 3 web pages, one for the home, one for the content, one for the properties.
The main focus of our business is to offer non performing loans (before foreclosures) to the general public. All the non-performing mortgages will end in a house, an apartment, a store, etc.
Our customers are able to invest from 10,000usd to 1,000,000usd (average 50,000usd).
Our customers' usual focus groups are employees who want second earnings, perceiving the business feeling without outlay time. They look for a solid finance sense corporation that confers them certainty.
Nearly all our clients desire the house, apartment, store, etc. more than the actual earnings.
The name of our company is BRAMLEY
Reason: We value the time and effort you already invest in our project. We realize that we did't come back on some of the doubts requested by the designers. It will be inequitable to the designers who prerequisite our feedback. We also appreciate the comprehension of the community in this postponement.
Reason: Designers,
We really apreciate all the time and effort you put on our project. From the begining we ask for 3 pages, so now we will leave the 10 finalist and provide some extra time to submit the other 2 pages.
We will race the price in 10%
Target Market(s)
Our customers average investors works as employees and want to have a second income or business without spending time. (People from 35 to 50)
Industry/Entity Type
Finance
Requirements
Should not have
- FLASH

```html
<!DOCTYPE html>
<html lang="en">
<head>
<meta charset="utf-8">
<title>BRAMLEY – Non-performing mortgages</title>
<link href="https://fonts.googleapis.com/css2?family=PT+Sans:wght@400;700&family=PT+Sans+Narrow:wght@400;700&family=Arimo:wght@400;700&display=swap" rel="stylesheet">
<style>
  :root{
    --bg:#17181c;
    --bg-top:#222328;
    --header:#1b1c20;
    --panel:#2c2d33;
    --panel-dark:#202126;
    --field:#3a3b41;
    --red:#e3120b;
    --red-dark:#a80c07;
    --grey-head:#8d8b88;
    --grey-text:#b6b4b0;
    --white:#ffffff;
    --nav-bg:#ececec;
    --nav-text:#111111;
    --logo-bg:#d4d4d4;
    --logo-text:#3a3a3a;
    --line:#34353b;
  }
  *{box-sizing:border-box;margin:0;padding:0}
  html,body{width:979px;height:1200px;overflow:hidden;background:var(--bg)}
  body{position:relative;font-family:"Arimo",Arial,sans-serif;color:var(--white)}
  .abs{position:absolute}

  .topbar{left:0;top:0;width:979px;height:35px;background:repeating-linear-gradient(135deg,#26272c 0 2px,#1f2024 2px 4px)}
  .follow{left:680px;top:10px;font:700 13px "PT Sans Narrow",sans-serif;color:#8a8a8a;letter-spacing:.3px}
  .social{top:8px;width:20px;height:20px;background:#5a5b60;border-radius:2px}

  .header{left:0;top:35px;width:979px;height:110px;background:radial-gradient(ellipse at 45% 40%,#2e2f34 0,var(--header) 70%)}
  .site-title{left:69px;top:64px;font:400 43px "PT Sans",sans-serif;color:var(--red);letter-spacing:-1.5px}
  .search{left:683px;top:78px;width:226px;height:32px;background:#0e0f12;border-left:4px solid #3b3c41}
  .search span{position:absolute;left:10px;top:8px;font:400 14px "Arimo",sans-serif;color:#d8d8d8}
  .search-btn{position:absolute;right:0;top:0;width:28px;height:32px;background:#3a3b40}

  .hero{left:69px;top:158px;width:840px;height:313px;background:linear-gradient(110deg,#3c3d42 0%,#8e8f93 28%,#2c2d31 55%,#1b1c1f 100%)}
  .hero-photo{position:absolute;left:0;top:0;width:640px;height:313px;background:radial-gradient(circle at 30% 45%,#bfc0c2 0,#6a6b6f 30%,#8b1a17 48%,#2a2b2f 75%)}
  .logo-box{left:706px;top:159px;width:202px;height:198px;background:var(--logo-bg);display:flex;align-items:center;justify-content:center;gap:10px}
  .logo-box .mark{width:22px;height:22px;background:var(--logo-text)}
  .logo-box .name{font:700 34px "PT Sans Narrow",sans-serif;color:var(--logo-text)}
  .hero-next{left:849px;top:371px}

  .nav{left:69px;top:484px;width:840px;height:72px;background:repeating-linear-gradient(135deg,#f4f4f4 0 2px,#e6e6e6 2px 4px);border-bottom:5px solid #cfcfcf}
  .nav-item{position:absolute;top:27px;transform:translateX(-50%);font:700 20px "PT Sans Narrow",sans-serif;color:var(--nav-text);letter-spacing:-.3px;white-space:nowrap}
  .nav-tab{position:absolute;top:-4px;width:20px;height:20px;transform:translateX(-50%);background:#fff;border:1px solid #ddd}

  .panel-head{left:69px;width:316px;height:47px;background:var(--panel)}
  .panel-head .title{position:absolute;left:14px;top:12px;font:400 19px "PT Sans Narrow",sans-serif;color:var(--grey-head);letter-spacing:-.3px}
  .panel-head b{color:var(--white)}
  .panel-head .grip{position:absolute;right:0;top:0;width:42px;height:47px;background:var(--panel-dark)}
  .field{height:30px;background:var(--field);font:400 14px "Arimo",sans-serif;color:#e6e6e6;padding:7px 7px}
  .field.select::after{content:"";position:absolute;right:9px;top:12px;border-left:6px solid transparent;border-right:6px solid transparent;border-top:7px solid #e6e6e6}
  .btn-search{left:261px;top:845px;width:110px;height:29px;background:linear-gradient(#d8221b,var(--red-dark));border-radius:3px;font:700 16px "PT Sans Narrow",sans-serif;text-align:center;line-height:29px}

  .pm-list{left:86px;top:963px;list-style:none}
  .pm-list li{height:25.3px;font:400 12px "Arimo",sans-serif;color:var(--grey-text);text-decoration:underline;letter-spacing:.3px}
  .pm-list li::before{content:"+";color:var(--red);font-weight:700;margin-right:9px;text-decoration:none;display:inline-block}

  .sec-title{font:400 29px "PT Sans Narrow",sans-serif;color:var(--grey-head);letter-spacing:-.5px;line-height:1}
  .sec-title .hl{color:var(--red)}
  .sec-title b{color:var(--red)}
  .sec-sub{font:700 11px "PT Sans Narrow",sans-serif;color:#8a8a8a;letter-spacing:.3px}

  .thumb{width:202px;height:86px;border:3px solid #9a9a9a;background:linear-gradient(180deg,#a9c4e0 0 35%,#d8d2c6 35% 70%,#6b7f52 70%)}
  .thumb-btn{position:absolute;right:-8px;bottom:-10px;width:110px;height:30px;background:linear-gradient(#4a4b50,#222327);border-radius:3px;font:700 15px "PT Sans Narrow",sans-serif;text-align:center;line-height:30px}
  .card-title{font:700 15px "Arimo",sans-serif;color:var(--grey-head)}
  .card-body{width:210px;font:400 13.5px/20px "Arimo",sans-serif;color:var(--white)}
  .card-body a{color:var(--red)}
  .read-more{font:700 14px "PT Sans Narrow",sans-serif;color:var(--grey-head);display:flex;align-items:center;gap:6px}

  .finance-icon{left:442px;top:966px;width:73px;height:76px;background:radial-gradient(circle at 50% 40%,#9a9a9a 0,#5a5a5a 45%,#c9a337 70%,transparent 72%)}
  .finance-text{left:533px;top:968px;width:340px;font:400 13.5px/20px "Arimo",sans-serif}
  .finance-text b{color:var(--grey-head)}
  .finance-link{left:442px;top:1058px;width:450px;font:400 13.5px/20px "Arimo",sans-serif;color:var(--red);text-decoration:underline}

  .footer{left:0;top:1134px;width:979px;height:66px;background:repeating-linear-gradient(135deg,#1d1e22 0 2px,#18191c 2px 4px);border-top:1px dashed var(--line)}
  .footer-links{left:69px;top:1150px;font:400 12px "Arimo",sans-serif;color:var(--white)}
  .copyright{left:69px;top:1168px;font:400 12px "Arimo",sans-serif;color:var(--white)}
</style>
</head>
<body>

<div class="abs topbar"></div>
<div class="abs follow">FOLLOW US ON</div>
<div class="abs social" style="left:788px"></div>
<div class="abs social" style="left:813px"></div>
<div class="abs social" style="left:839px"></div>
<div class="abs social" style="left:864px"></div>
<div class="abs social" style="left:889px"></div>

<div class="abs header"></div>
<h1 class="abs site-title">Non-performing mortgages</h1>
<div class="abs search"><span>SEARCH</span><div class="search-btn">
  <svg width="28" height="32"><path d="M11 10 L18 16 L11 22 Z" fill="#8a8a8a"/></svg></div></div>

<div class="abs hero">
  <div class="hero-photo" role="img" aria-label="Red-roofed model houses under a large magnifying glass"></div>
</div>
<div class="abs logo-box"><span class="mark"></span><span class="name">BRAMLEY</span></div>
<svg class="abs hero-next" width="20" height="20"><circle cx="10" cy="10" r="9" fill="#e8e8e8" stroke="#999"/><path d="M8 5.5 L13 10 L8 14.5 Z" fill="#333"/></svg>

<nav class="abs nav">
  <span class="nav-tab" style="left:93px"></span><span class="nav-item" style="left:93px">HOME PAGE</span>
  <span class="nav-tab" style="left:237px"></span><span class="nav-item" style="left:237px">ABOUT US</span>
  <span class="nav-tab" style="left:365px"></span><span class="nav-item" style="left:365px">SELLING</span>
  <span class="nav-tab" style="left:489px"></span><span class="nav-item" style="left:489px">RENTING</span>
  <span class="nav-tab" style="left:618px"></span><span class="nav-item" style="left:618px">SERVICES</span>
  <span class="nav-tab" style="left:753px"></span><span class="nav-item" style="left:753px">CONTACTS</span>
</nav>

<div class="abs panel-head" style="top:582px"><span class="title"><b>FIND</b> PROPERTY</span><span class="grip"></span></div>
<div class="abs field" style="left:83px;top:648px;width:288px">City &amp; State, or Zip</div>
<div class="abs field select" style="left:83px;top:697px;width:288px">Search Area</div>
<div class="abs field select" style="left:83px;top:746px;width:134px">Price from</div>
<div class="abs field select" style="left:237px;top:746px;width:134px">to</div>
<div class="abs field select" style="left:83px;top:796px;width:134px">Bedrooms</div>
<div class="abs field select" style="left:237px;top:796px;width:134px">Bathrooms</div>
<div class="abs btn-search">SEARCH NOW</div>

<div class="abs panel-head" style="top:898px"><span class="title"><b>PROPERTY</b> MANAGEMENT</span><span class="grip"></span></div>
<ul class="abs pm-list">
  <li>LOREM IPSUM DOLOR SIT AMET,</li>
  <li>CONSECTETUER ADIPISCING ELIT. NAM EU</li>
  <li>NULLA. DONEC LOBORTIS PURUS VEL</li>
  <li>URNA. NUNC LAOREET LACINIA NUNC. IN</li>
  <li>VOLUTPAT SODALES IPSUM. SED</li>
  <li>VESTIBULUM. INTEGER IN ANTE. SED</li>
</ul>

<h2 class="abs sec-title" style="left:442px;top:586px"><span class="hl">FEATURED</span> PROPERTIES</h2>
<div class="abs sec-sub" style="left:442px;top:612px">LOREM IPSUM DOLOR SIT AMET, LOREM</div>

<div class="abs thumb" style="left:442px;top:643px" role="img" aria-label="Two-storey suburban house with a front lawn"><span class="thumb-btn">VIEW IMAGES</span></div>
<div class="abs card-title" style="left:442px;top:752px">Lorem ipsum dolor sit amet</div>
<p class="abs card-body" style="left:442px;top:776px">Consectetuer adipiscing elit. Nam urna. Nunc <a href="#">laoreet lacinia</a> nunc. In volutpat sodales ipsum.</p>
<div class="abs read-more" style="left:542px;top:850px"><svg width="16" height="16"><circle cx="8" cy="8" r="7.5" fill="#8d8b88"/><path d="M8 4v8M4 8h8" stroke="#17181c" stroke-width="2"/></svg>READ MORE</div>

<div class="abs thumb" style="left:683px;top:643px" role="img" aria-label="Brick family house with a white garage door"><span class="thumb-btn">VIEW IMAGES</span></div>
<div class="abs card-title" style="left:683px;top:752px">Lorem ipsum dolor sit amet</div>
<p class="abs card-body" style="left:683px;top:776px">Consectetuer adipiscing elit. Nam eu nulla <a href="#">lorem ipsum</a> Donec sed nunc. In volutpat sodales ipsum.</p>
<div class="abs read-more" style="left:783px;top:850px"><svg width="16" height="16"><circle cx="8" cy="8" r="7.5" fill="#8d8b88"/><path d="M8 4v8M4 8h8" stroke="#17181c" stroke-width="2"/></svg>READ MORE</div>

<h2 class="abs sec-title" style="left:442px;top:902px"><b>FINANCE</b> PROGRAMS</h2>
<div class="abs sec-sub" style="left:442px;top:928px">LOREM IPSUM DOLOR SIT AMET,</div>
<div class="abs finance-icon" role="img" aria-label="Steel safe with stacks of gold coins"></div>
<p class="abs finance-text"><b>Lorem ipsum dolor sit amet, consectetuer</b> adipiscing elit. Nam eu nulla.vel urna. Nunc laoreet lacinia nunc. In volutpat sodales ipsum. Sed vestibulum.</p>
<p class="abs finance-link">Lorem ipsum dolor sit amet, consectetuer adipiscing elit. Nam eu nulla, sodales ipsum. Sed vestibulum. Integer in ante.</p>

<footer class="abs footer"></footer>
<div class="abs footer-links">HOME | ABOUT US | SELLING | RENTING &nbsp;| SERVICES | CONTACTS</div>
<div class="abs copyright">Copyright © Your Company Name</div>

</body>
</html>
```